Renewal of the Ferravolt SA Website

Ferravolt SA is a metal construction company active in industrial piping, boilermaking and metal framing. We would like to renew our site.

This website must be ready to work with Wordpress.

The site will contain the following pages: Home, skills, presentation, contact.

The site must reflect the field of the metal construction sector. It must be clear and easily understandable. The objective is not to win mandates with but to present the company and its capabilities.

I have inserted the pages of our old presentations, to describe our sector but we do not want to reuse these elements, we are waiting for your creativity to surprise us. In the 2nd phase we will complete with new images if necessary and texts

Target Market(s)

International companies in the food, chemical and pharmaceutical sectors

Industry/Entity Type

Alimentaire, pharma, chimie

Number of Pages Required

4 page

Font styles to use
Sans Serif

Colors
0054AA
0677BA
7BADD7
CADEEF
E8F1F8

Requirements
Must have
• It must contain at least the requested pages, images of illustrations, places for descriptions
Should not have
• Elements that appear or disappear, too flash,

```html
<!DOCTYPE html>
<html lang="en">
<head>
<meta charset="utf-8">
<title>Ferravolt SA — Metal Construction</title>
<link href="https://fonts.googleapis.com/css2?family=Montserrat:wght@400;500;600;700;800&display=swap" rel="stylesheet">
<style>
:root{
  --brand:#1f4aa8;
  --brand-dark:#1a3d8f;
  --navy:#232a6e;
  --ink:#111;
  --muted:#6b6b6b;
  --charcoal:#3b3b3b;
  --footer:#0f0f10;
  --light:#e8f1f8;
  --sky:#7badd7;
  --star:#f5b400;
}
*{box-sizing:border-box;margin:0;padding:0}
html,body{width:1200px;height:3819px;overflow:hidden}
body{position:relative;font-family:'Montserrat',sans-serif;color:var(--ink);background:#fff}
.abs{position:absolute}
a{color:inherit;text-decoration:none}
.btn{position:absolute;display:flex;align-items:center;justify-content:center;border-radius:24px;font-weight:700;font-size:16px;color:#fff;background:var(--brand)}
.btn.dark{background:var(--charcoal)}

/* header */
.site-header{position:absolute;left:0;top:0;width:1200px;height:86px;background:#f7f9fc}
.brand{position:absolute;display:flex;align-items:center;gap:12px;font-weight:800;color:var(--navy)}
.brand .mark{border-radius:50%;background:var(--navy)}
.nav{position:absolute;top:36px;font-size:13px;font-weight:600;letter-spacing:.3px}

/* hero */
.hero{position:absolute;left:0;top:86px;width:1200px;height:555px;
  background:linear-gradient(100deg,rgba(40,30,25,.85) 0%,rgba(60,45,40,.55) 35%,rgba(40,60,90,.35) 70%,rgba(30,50,80,.6) 100%),
  linear-gradient(180deg,#8a6a5a 0%,#4c5a6e 45%,#6c4a3a 75%,#2d3340 100%)}
.hero h2{position:absolute;left:111px;top:130px;color:#fff;font-size:28px;font-weight:700}
.hero h1{position:absolute;left:111px;top:168px;color:#fff;font-size:46px;font-weight:800;letter-spacing:.5px}
.hero p{position:absolute;left:111px;top:232px;width:380px;color:#fff;font-size:16px;line-height:26px}

/* sections */
.section-title{position:absolute;left:0;width:1200px;text-align:center;font-size:40px;font-weight:800;color:var(--navy)}
.lead{position:absolute;text-align:center;font-size:16px;line-height:26px;color:#555}
.skill-card{position:absolute;top:893px;width:299px;height:319px;background:#fff;box-shadow:0 2px 8px rgba(0,0,0,.12);border-bottom:3px solid var(--brand)}
.skill-card .icon{position:absolute;left:15px;top:-25px;width:98px;height:98px;border-radius:50%;background:#fff;box-shadow:0 3px 8px rgba(0,0,0,.15);display:flex;align-items:center;justify-content:center}
.skill-card h3{position:absolute;left:18px;top:112px;font-size:22px;font-weight:700}
.skill-card p{position:absolute;left:18px;top:156px;width:270px;font-size:13.5px;line-height:26px;color:var(--muted)}

.about{position:absolute;left:0;top:1315px;width:1200px;height:523px;background:linear-gradient(120deg,#2a57b3 0%,#2350ab 50%,#2b58b2 100%)}
.photo{position:absolute;border-radius:4px}
.about h2{position:absolute;left:599px;top:85px;color:#fff;font-size:40px;font-weight:800}
.about p{position:absolute;left:599px;top:150px;width:440px;color:#fff;font-size:14.5px;line-height:26px}

.pres h2{position:absolute;left:111px;top:1925px;font-size:40px;font-weight:800;color:var(--navy)}
.pres p{position:absolute;left:111px;top:1990px;width:440px;font-size:14.5px;line-height:26px;color:var(--muted)}

.testimonial{position:absolute;top:2458px;height:357px;background:#fff;box-shadow:0 1px 6px rgba(0,0,0,.18);border-radius:4px;text-align:center}
.testimonial .avatar{position:absolute;top:19px;width:110px;height:110px;border-radius:50%;left:50%;margin-left:-55px}
.testimonial .name{position:absolute;left:0;width:100%;top:140px;font-size:17px;font-weight:500}
.testimonial .role{position:absolute;left:0;width:100%;top:165px;font-size:14px;color:var(--brand)}
.testimonial .q{position:absolute;left:10px;top:172px;font-size:40px;font-weight:800;font-family:Georgia,serif}
.testimonial p{position:absolute;left:20px;right:20px;top:204px;font-size:14px;line-height:26px;color:var(--muted)}
.testimonial .stars{position:absolute;left:0;width:100%;top:314px;color:var(--star);font-size:19px;letter-spacing:1px}
.arrow{position:absolute;top:2595px;width:22px;height:22px;border-radius:50%;display:flex;align-items:center;justify-content:center}

.quote{position:absolute;left:0;top:2907px;width:1200px;height:536px;background:linear-gradient(120deg,#2654b0 0%,#1f49a3 55%,#2b59b4 100%)}
.quote h2{position:absolute;left:0;width:100%;top:90px;text-align:center;color:#fff;font-size:40px;font-weight:800}
.contact-item{position:absolute;left:111px;display:flex;align-items:flex-start;gap:10px;color:#fff;font-size:14.5px;font-weight:600;line-height:26px}
.contact-item .ci{flex:none;width:38px;height:38px;border:2px solid #fff;border-radius:50%;display:flex;align-items:center;justify-content:center}
.field{position:absolute;background:#fff;border-radius:4px;font-size:13px;color:#777;padding:14px 16px}

.site-footer{position:absolute;left:0;top:3443px;width:1200px;height:376px;background:var(--footer);color:#fff}
.site-footer h4{position:absolute;top:90px;font-size:24px;font-weight:700}
.site-footer ul{position:absolute;list-style:none;font-size:14px;line-height:30px}
.social{position:absolute;top:167px;width:30px;height:30px;border:1.5px solid #fff;border-radius:50%}
.footer-rule{position:absolute;left:110px;top:316px;width:976px;height:1px;background:#888}
.copyright{position:absolute;left:0;width:100%;top:334px;text-align:center;font-size:14px}
</style>
</head>
<body>

<header class="site-header">
  <div class="brand" style="left:111px;top:20px;font-size:30px">
    <span class="mark" style="width:46px;height:46px"></span>Ferravolt SA
  </div>
  <nav>
    <a class="nav" style="left:557px">HOME</a>
    <a class="nav" style="left:632px">SKILLS</a>
    <a class="nav" style="left:711px">PRESENTATION</a>
    <a class="nav" style="left:847px">CONTACT</a>
  </nav>
  <a class="btn" style="left:936px;top:21px;width:151px;height:44px">Get A Quote</a>
</header>

<section class="hero" role="img" aria-label="Industrial plant interior with insulated pipelines and valves">
  <h2>WELCOME TO</h2>
  <h1>FERRAVOLT</h1>
  <p>Lorem Ipsum is simply dummy text of the printing and typesetting industry. Lorem Ipsum</p>
  <a class="btn" style="left:111px;top:304px;width:150px;height:44px">Get Started</a>
</section>

<h2 class="section-title" style="top:725px">OUR SKILLS</h2>
<p class="lead" style="left:210px;top:788px;width:780px">Lorem Ipsum is simply dummy text of the printing and typesetting industry. Lorem Ipsum has been the industry's standard dummy text ever since the 1500s,</p>

<article class="skill-card" style="left:111px">
  <div class="icon">
    <svg width="70" height="58" viewBox="0 0 70 58" fill="#1f4aa8"><rect x="22" y="2" width="26" height="6" rx="2"/><rect x="32" y="8" width="6" height="12"/><rect x="22" y="18" width="26" height="34" rx="4"/><rect x="2" y="28" width="16" height="24"/><rect x="52" y="28" width="16" height="24"/></svg>
  </div>
  <h3>Industrial Piping</h3>
  <p>Lorem Ipsum is simply dummy text of the printing and typesetting industry. Lorem Ipsum has been the industry's standard dummy text ever since the 1500s, when an unknown printer took</p>
</article>
<article class="skill-card" style="left:449px">
  <div class="icon">
    <svg width="66" height="66" viewBox="0 0 66 66" fill="none" stroke="#1f4aa8" stroke-width="3"><rect x="10" y="18" width="20" height="40" rx="3"/><rect x="36" y="18" width="20" height="40" rx="3"/><rect x="15" y="26" width="10" height="8"/><rect x="41" y="26" width="10" height="8"/><circle cx="20" cy="46" r="3"/><circle cx="46" cy="46" r="3"/><path d="M20 18V8h26v10M4 12h8"/></svg>
  </div>
  <h3>Boiler Making</h3>
  <p>Lorem Ipsum is simply dummy text of the printing and typesetting industry. Lorem Ipsum has been the industry's standard dummy text ever since the 1500s, when an unknown printer took</p>
</article>
<article class="skill-card" style="left:787px">
  <div class="icon">
    <svg width="60" height="60" viewBox="0 0 60 60" fill="#1f4aa8"><path d="M30 4h22L26 56H4z"/><path d="M20 40l8-14 6 0-8 14z" fill="#fff"/></svg>
  </div>
  <h3>Metal Framing</h3>
  <p>Lorem Ipsum is simply dummy text of the printing and typesetting industry. Lorem Ipsum has been the industry's standard dummy text ever since the 1500s, when an unknown printer took</p>
</article>

<section class="about">
  <div class="photo" style="left:130px;top:85px;width:211px;height:169px;background:linear-gradient(135deg,#6b7480,#3c4a63)" role="img" aria-label="Worker in hard hat assembling a flanged pipe"></div>
  <div class="photo" style="left:348px;top:85px;width:211px;height:169px;background:linear-gradient(135deg,#a58a6c,#5d4e40)" role="img" aria-label="Workshop interior with ladders and timber structure"></div>
  <div class="photo" style="left:133px;top:272px;width:428px;height:170px;background:linear-gradient(160deg,#c9a98a,#7d6a5a 55%,#4c4f58)" role="img" aria-label="Welder working on a large pipeline outdoors"></div>
  <h2>ABOUT US</h2>
  <p>Lorem Ipsum is simply dummy text of the printing and typesetting industry. Lorem Ipsum has been the industry's standard dummy text ever since the 1500s, when an unknown printer took a galley of type and scrambled it to make a type specimen book. It has survived not only five centuries, but also the leap into electronic typesetting, remaining essentially unchanged.Lorem Ipsum is simply dummy text of the printing and typesetting industry. Lorem Ipsum has been the industry's</p>
  <a class="btn dark" style="left:599px;top:384px;width:150px;height:45px">Get Started</a>
</section>

<section class="pres">
  <h2>OUR PRESENTATIONS</h2>
  <p>Lorem Ipsum is simply dummy text of the printing and typesetting industry. Lorem Ipsum has been the industry's standard dummy text ever since the 1500s, when an unknown printer took a galley of type and scrambled it to make a type specimen book. It has survived not only five centuries, but also the leap into electronic typesetting, remaining essentially unchanged.Lorem Ipsum is simply dummy text of the printing and typesetting industry. Lorem Ipsum has been the industry's</p>
  <a class="btn" style="left:111px;top:2221px;width:151px;height:44px">Read More</a>
  <svg class="abs" style="left:638px;top:2094px" width="234" height="200"><path d="M30 2H14a12 12 0 0 0-12 12v184h228v-30" fill="none" stroke="#1f4aa8" stroke-width="2"/></svg>
  <div class="abs" style="left:674px;top:1936px;width:381px;height:323px;background:#fff;box-shadow:0 2px 10px rgba(0,0,0,.12)"></div>
  <div class="abs" style="left:674px;top:1956px;width:381px;height:284px;background:linear-gradient(90deg,#7badd7 0%,#7badd7 36%,#e8f1f8 36%,#cadeef 100%)" role="img" aria-label="Company brochure page on industrial piping with photos of installations"></div>
</section>

<h2 class="section-title" style="top:2376px">TESTIMONIALS</h2>
<div class="arrow" style="left:29px;background:#9a9a9a"><svg width="10" height="10"><path d="M7 1L3 5l4 4" stroke="#fff" stroke-width="2" fill="none"/></svg></div>
<div class="arrow" style="left:1134px;background:var(--brand)"><svg width="10" height="10"><path d="M3 1l4 4-4 4" stroke="#fff" stroke-width="2" fill="none"/></svg></div>

<article class="testimonial" style="left:110px;width:312px">
  <div class="avatar" style="background:#f0c9a4" role="img" aria-label="Portrait of Anderson"></div>
  <div class="name">Anderson</div><div class="role">Client</div><div class="q">“</div>
  <p>Lorem Ipsum is simply dummy text of the printing and typesetting industry. Lorem Ipsum has been the industry's standard dummy text ever since the</p>
  <div class="stars">★★★★★</div>
</article>
<article class="testimonial" style="left:441px;width:315px">
  <div class="avatar" style="background:#c9d7e4" role="img" aria-label="Portrait of Robin"></div>
  <div class="name">Robin</div><div class="role">Client</div><div class="q">“</div>
  <p>Lorem Ipsum is simply dummy text of the printing and typesetting industry. Lorem Ipsum has been the industry's standard dummy text ever since the</p>
  <div class="stars">★★★★★</div>
</article>
<article class="testimonial" style="left:773px;width:313px">
  <div class="avatar" style="background:#e6e3e0" role="img" aria-label="Portrait of Jessica"></div>
  <div class="name">jessica</div><div class="role">Client</div><div class="q">“</div>
  <p>Lorem Ipsum is simply dummy text of the printing and typesetting industry. Lorem Ipsum has been the industry's standard dummy text ever since the</p>
  <div class="stars">★★★★★</div>
</article>

<section class="quote">
  <h2>GET A QUOTE</h2>
  <div class="contact-item" style="top:186px">
    <span class="ci"><svg width="14" height="18" viewBox="0 0 14 18"><path d="M7 1a6 6 0 0 0-6 6c0 4.5 6 10 6 10s6-5.5 6-10a6 6 0 0 0-6-6z" fill="none" stroke="#fff" stroke-width="2"/><circle cx="7" cy="7" r="2" fill="#fff"/></svg></span>
    <span>Lorem ipsum Lorem Ipsum<br>Lorem Ipsum</span>
  </div>
  <div class="contact-item" style="top:246px;align-items:center">
    <span class="ci"><svg width="16" height="16" viewBox="0 0 16 16"><path d="M3 1l3 3-2 2c1 2 3 4 5 5l2-2 3 3-2 3C7 14 2 9 1 3z" fill="#fff"/></svg></span>
    <span>+1 555 010 2040</span>
  </div>
  <div class="contact-item" style="top:303px;align-items:center">
    <span class="ci"><svg width="18" height="14" viewBox="0 0 18 14"><rect x="1" y="1" width="16" height="12" fill="none" stroke="#fff" stroke-width="2"/><path d="M1 1l8 7 8-7" fill="none" stroke="#fff" stroke-width="2"/></svg></span>
    <span>info@ferravolt.com</span>
  </div>
  <div class="field" style="left:553px;top:171px;width:257px;height:46px">First Name</div>
  <div class="field" style="left:827px;top:171px;width:257px;height:46px">Last Name</div>
  <div class="field" style="left:553px;top:226px;width:257px;height:46px">Email</div>
  <div class="field" style="left:827px;top:226px;width:257px;height:46px">Phone</div>
  <div class="field" style="left:553px;top:284px;width:531px;height:96px">Message</div>
  <a class="btn dark" style="left:553px;top:395px;width:145px;height:45px">Submit</a>
</section>

<footer class="site-footer">
  <div class="brand" style="left:111px;top:100px;font-size:22px;color:#fff;gap:10px">
    <span class="mark" style="width:28px;height:28px;background:#fff"></span>Ferravolt
  </div>
  <span class="social" style="left:112px"></span>
  <span class="social" style="left:164px"></span>
  <span class="social" style="left:215px"></span>

  <h4 style="left:381px">Quick links</h4>
  <ul style="left:384px;top:130px"><li>Home</li><li>Skills</li><li>Presentation</li><li>Contact.</li></ul>

  <h4 style="left:612px">Other links</h4>
  <ul style="left:612px;top:130px;line-height:27px"><li>Privacy Policy</li><li>Careers</li><li>Terms Condition</li></ul>

  <h4 style="left:861px">Contact Info</h4>
  <ul style="left:861px;top:130px;line-height:28px">
    <li>✉ info@ferravolt.com</li>
    <li>☎ +1 555 010 2040</li>
    <li>⌖ lorem ipsum</li>
    <li style="padding-left:18px">ipsum lorem Ipsum</li>
  </ul>
  <div class="footer-rule"></div>
  <div class="copyright">Copyright © 2023 Ferravolt | All Rights Reserved</div>
</footer>

</body>
</html>
```